Corporate Two Sided Business Card

Looking for a Corporate "edgy" Modern look and feel for a business card

We are looking at two options. Dark background with our logo on it, white background with our logo on it - The background is more - Charcoal / Graphite then black

Details will be

Danielle Forsk

Licensee / Director

m. 0428 519 064

e. danielle@quorvela.com.au

quorvela.com.au

Target Market(s)

Professional Business people that refer use business and clients that own Investment Properties

Industry/Entity Type

Business

Contact Information for Business Card

Details will be

Danielle Forsk

Licensee / Director

m. 0428 519 064

quorvela.com.au

Font styles to use
Serif

Colors
000000
ec1f27
eeeeee
ffffff

Requirements
Must have
• Two options - White Background and Dark Background. - Two sided
Nice to have
• A design that is edgy, modern and new to look instead of boring style corporate cards - It should be a full integrated design
Should not have
• Block looking - Cheap.

```html
<!DOCTYPE html>
<html lang="en">
<head>
<meta charset="utf-8">
<title>Quorvela Business Card</title>
<link rel="stylesheet" href="https://fonts.googleapis.com/css2?family=Montserrat:wght@400;700&display=swap">
<style>
  :root {
    --backdrop: #111111;
    --card: #1b1b1b;
    --card-edge: #242424;
    --ink: #050505;
    --ink-soft: #0b0b0b;
  }
  * { margin: 0; padding: 0; box-sizing: border-box; }
  html, body {
    width: 1200px; height: 1000px; overflow: hidden;
    background: var(--backdrop);
    font-family: "Montserrat", Arial, sans-serif;
  }
  .stage {
    position: relative; width: 1200px; height: 1000px;
  }
  .card {
    position: absolute; top: 350px;
    width: 520px; height: 300px;
    background: var(--card);
    border: 1px solid var(--card-edge);
    border-radius: 22px;
    box-shadow: 0 10px 30px rgba(0,0,0,0.5);
  }
  .card-front { left: 50px; }
  .card-back { left: 630px; }

  .brand {
    display: flex; align-items: center; gap: 10px;
    color: var(--ink); font-weight: 700; letter-spacing: 0.5px;
  }
  .brand-mark {
    width: 0.7em; height: 0.7em; background: var(--ink);
  }
  .card-front .brand {
    position: absolute; left: 50%; top: 50%;
    transform: translate(-50%, -50%);
    font-size: 52px;
  }
  .card-back .brand {
    position: absolute; left: 40px; top: 34px;
    font-size: 46px;
  }
  .holder {
    position: absolute; left: 40px; top: 124px; color: var(--ink);
  }
  .holder-name { font-size: 26px; font-weight: 700; }
  .holder-role { font-size: 14px; font-weight: 400; color: var(--ink-soft); margin-top: 2px; }
  .contact {
    position: absolute; left: 40px; top: 206px;
    list-style: none; color: var(--ink-soft);
    font-size: 15px; line-height: 21px;
  }
</style>
</head>
<body>
  <main class="stage">
    <section class="card card-front" aria-label="Card front">
      <div class="brand"><span class="brand-mark"></span>quorvela</div>
    </section>
    <section class="card card-back" aria-label="Card back">
      <div class="brand"><span class="brand-mark"></span>quorvela</div>
      <div class="holder">
        <p class="holder-name">Danielle Forsk</p>
        <p class="holder-role">Licensee / Director</p>
      </div>
      <ul class="contact">
        <li>0428 519 064</li>
        <li>danielle@quorvela.com.au</li>
        <li>quorvela.com.au</li>
      </ul>
    </section>
  </main>
</body>
</html>
```